Modern Website For Law Firm Lawyer Melbourne, Australia Coded

We are looking for a modern and sophisticated website design. We would prefer the site to be based on WordPress given it is intuitive and some of our staff have experience using it.

Our law firm is based in Melbourne, Australia and we deal with property. The website must be hosted on a reliable Australian server.

We would also appreciate it if the designer can provide some guidance about how to make changes/upload content, such as photos and articles. We are happy to pay for this advice.

We prefer classic fonts in black or grey. We would also like a dash of colour so please use a green, blue or aqua colour palette that is consistent with our logo attached.

We do not want any law related images - scales of justice, gavel or the like.

Our ultimate goal is to communicate that the firm is professional, affordable, modern, dynamic, knowledgeable and one with the community.

We would like the following pages/sections/icons:

1. Who We Are - we will provide content.

2. Our Services - 1. Property 2. Wills, 3. Powers of Attorney 4. Probate & Estate Administration 5.Consultancy & Agency- we will provide content for each of these sections.

3. Articles - we already have approximately 20 articles on a wordpress blog and would like to port these articles to the website. We can do this ourselves if the designer can give us instructions about how to do this. We would also like to give clients the option to subscribe to our articles.

4. Contact Us - this should include our firms contact details; location map and we would like to give clients the option to "Request A Quote" directly from the page - i.e they will need to provide their full name, phone number email address, choose subject from drop down menu and type a message that gets sent to our outlook email.

5. Terms and Conditions - we will provide content

We really like the style and photographs used in the following website and want something as close to this as possible:

https://www.brelwick.com/

For privacy reasons, we would prefer to provide content together with all business details once we have decided on the winner.

We will monitor entries closely and promise to provide feedback and guidance on each entry.

This project is guaranteed. If our budget is too low please email us so we can discuss further and perhaps increase our budget. We are reasonable in this regard.

Thank you very much for considering this project.

Target Market(s)

General public, professionals, lawyers and conveyancers

Industry/Entity Type

Law Firm

Coding

Coded - Design and coding required

Number of Pages Required

1 page

Font styles to use
Sans Serif

Colors
33b8a4
33a6d7
0692cd
3176b5
00a990
9bcb3c
86cfc6
cadf82
85acd3

Requirements
Must have
• 1. Site must be coded and hosted on a reliable Australian server and it would be much appreciated if the deisgner provides instructions about how to add photos, blog articles etc-
• 2. The site must be secure and have green lock at top of page
• 3. Request A Quote - name, email, phone, drop down subject, message - email to our outlook email
• 4. Article Subscription
• 5. Domain (we have already purchased)
• 6. Location map
• 7. Facebook, LinkedIn, Instagram Icons
• 8. Membership icons in this order - VLQ Member > Coastal Women Advocates > Guide For Counsel > Creature Foundation > Tovra > Parcelnet > Vek QA logos attached to go on bottom of page
• 9. Testimonials
Nice to have
• A modern, sophisticated website like:
• https://www.brelwick.com/ - we really like the style of the brelwick photographs
• We also really like this design by Rk of Sketch swarm:
• https://www.sketchswarm.com.au/design/58201946
Should not have
• Law related images - scales of justice gavel and the like

```html
<!DOCTYPE html>
<html lang="en">
<head>
<meta charset="utf-8">
<title>Calder Law</title>
<link href="https://fonts.googleapis.com/css2?family=Lato:wght@300;400;700;900&display=swap" rel="stylesheet">
<style>
:root{
  --teal:#17a98f;
  --teal-dark:#0f8f79;
  --ink:#2c3a44;
  --text:#3a3a3a;
  --muted:#8a8a8a;
  --soft:#f1f1f1;
  --line:#dcdcdc;
  --footer:#1d1d1d;
  --footer-deep:#141414;
  --white:#ffffff;
  --blue:#2a84c6;
}
*{box-sizing:border-box;margin:0;padding:0}
html,body{width:1200px;height:3377px;overflow:hidden}
body{font-family:"Lato",Arial,sans-serif;color:var(--text);background:var(--white);position:relative}
.abs{position:absolute}
.top-rule{position:absolute;left:0;top:0;width:1200px;height:8px;background:var(--teal)}

/* header */
.site-header{position:absolute;left:0;top:8px;width:1200px;height:127px;background:var(--white)}
.brand{position:absolute;left:28px;top:42px;display:flex;align-items:center;gap:12px}
.brand-dot{width:22px;height:22px;border-radius:50%;background:var(--teal)}
.brand-name{font-size:34px;font-weight:400;letter-spacing:3px;color:var(--ink)}
.brand-tag{position:absolute;left:62px;top:88px;font-size:9px;letter-spacing:2px;color:var(--muted)}
.util{position:absolute;right:52px;top:20px;display:flex;align-items:center;gap:8px;font-size:14px;color:var(--teal)}
.util .phone{margin-right:32px;display:flex;align-items:center;gap:6px}
.social{display:flex;gap:6px}
.social span{width:19px;height:19px;background:var(--teal);display:block}
.main-nav{position:absolute;top:72px;left:330px;display:flex;gap:0;font-size:14px;color:var(--ink);letter-spacing:.3px}
.main-nav a{color:var(--ink);text-decoration:none;position:absolute;white-space:nowrap}
.search-icon{position:absolute;left:1152px;top:76px}

/* hero */
.hero{position:absolute;left:0;top:135px;width:1200px;height:502px;
  background:linear-gradient(90deg,#f4f5f6 0%,#eceeef 35%,#b9b8b4 60%,#6f6a63 78%,#c9c6c0 100%)}
.hero h1{position:absolute;left:29px;top:86px;font-size:49px;line-height:60px;font-weight:700;color:var(--ink);letter-spacing:.2px}
.hero p{position:absolute;left:29px;top:220px;font-size:18px;color:var(--ink)}
.btn-outline{position:absolute;left:29px;top:283px;width:171px;height:55px;border:1px solid var(--ink);display:flex;align-items:center;justify-content:center;font-size:15px;color:var(--teal);background:rgba(255,255,255,.4)}

.section-title{position:absolute;left:0;width:1200px;text-align:center;font-size:24px;font-weight:400;letter-spacing:.5px;color:var(--ink)}

/* who we are */
.who{position:absolute;left:0;top:720px;width:1200px;height:372px;background:var(--soft)}
.who-photo{position:absolute;left:47px;top:50px;width:426px;height:270px;background:linear-gradient(135deg,#e6e6e6,#9a9a9a 60%,#d8d8d8)}
.who-panel{position:absolute;left:491px;top:0;width:709px;height:372px;background:var(--teal);color:var(--white)}
.who-panel p{position:absolute;left:122px;top:94px;width:540px;font-size:13px;line-height:20px}
.btn-white{position:absolute;left:122px;top:205px;width:135px;height:40px;background:var(--white);color:var(--teal);font-size:14px;display:flex;align-items:center;justify-content:center}

/* services */
.service{position:absolute;top:1200px;width:220px;text-align:center}
.service svg{display:block;margin:0 auto}
.service h3{font-size:14px;font-weight:400;color:var(--ink);margin-top:14px;line-height:20px;height:40px;letter-spacing:.3px}
.service p{font-size:11px;line-height:16px;color:var(--muted);margin-top:6px}
.service .more{display:inline-block;margin-top:10px;font-size:12px;color:var(--ink);border-bottom:2px solid var(--teal);padding-bottom:4px}

/* testimonials */
.testimonials{position:absolute;left:0;top:1545px;width:1200px;height:455px;background:var(--soft)}
.quote-mark{position:absolute;left:182px;top:85px}
.client-name{position:absolute;left:186px;top:173px;border-left:6px solid var(--muted);padding-left:12px;font-size:36px;font-weight:700;color:var(--teal);line-height:44px}
.client-quote{position:absolute;left:186px;top:242px;width:400px;font-size:16px;line-height:26px;font-style:italic;color:var(--muted)}
.slider-arrows{position:absolute;left:182px;top:320px;display:flex;gap:4px}
.slider-arrows span{width:32px;height:32px;background:var(--teal);display:flex;align-items:center;justify-content:center}
.client-grid{position:absolute;left:615px;top:44px;width:486px;height:364px;background:linear-gradient(135deg,#c8c8c8,#5e5e5e 50%,#b0b0b0)}

/* blog */
.post{position:absolute;top:2098px;width:319px}
.post-photo{width:319px;height:234px;background:linear-gradient(135deg,#ececec,#8c8c8c 55%,#dcdcdc);border:6px solid #eee}
.post h4{font-size:13px;font-weight:700;color:var(--ink);line-height:17px;margin-top:20px}
.blog-arrow{position:absolute;top:2283px}

/* contact */
.map{position:absolute;left:0;top:2500px;width:1200px;height:390px;background:linear-gradient(160deg,#e9efe3,#dfe7ee 45%,#cfe0ea 100%)}
.quote-form{position:absolute;left:26px;top:2540px;width:395px;height:309px;background:var(--teal);color:var(--white);padding:24px 22px}
.quote-form h3{font-size:17px;font-weight:400;letter-spacing:.5px}
.field{position:absolute;font-size:10px}
.field span{display:block;margin-bottom:3px}
.field i{display:block;height:18px;background:var(--white)}
.field b{display:block;font-weight:400;font-size:10px;color:var(--text);padding:3px 6px}
.send{position:absolute;right:22px;bottom:22px;width:84px;height:26px;background:var(--white);color:var(--teal);font-size:11px;display:flex;align-items:center;justify-content:center}

/* partners */
.partners{position:absolute;left:0;top:2948px;width:1200px;height:92px}
.badge{position:absolute;top:18px;height:58px;border-radius:6px}

/* footer */
.site-footer{position:absolute;left:0;top:3085px;width:1200px;height:252px;background:var(--footer);color:#d6d6d6}
.site-footer h5{font-size:14px;font-weight:700;color:var(--white);letter-spacing:.5px;border-bottom:1px solid #555;display:inline-block;padding-bottom:3px}
.about{position:absolute;left:47px;top:36px;width:370px}
.about p{font-size:11px;line-height:17px;margin-top:12px}
.about .line{display:flex;gap:10px;align-items:flex-start;margin-top:8px;font-size:11px;line-height:15px}
.links{position:absolute;left:498px;top:36px}
.links .cols{display:flex;gap:46px;margin-top:10px;font-size:11px;line-height:29px}
.links .social{margin-top:10px}
.links .social span{background:#444}
.newsletter{position:absolute;left:815px;top:36px;width:340px}
.newsletter h5{font-size:18px;font-weight:400;border:0}
.newsletter p{font-size:11px;line-height:17px;margin-top:12px;color:#aaa}
.subscribe{display:flex;margin-top:22px}
.subscribe .input{width:270px;height:30px;background:var(--white);font-size:10px;color:#aaa;padding:9px 8px}
.subscribe .btn{width:66px;height:30px;background:var(--teal);color:var(--white);font-size:12px;display:flex;align-items:center;justify-content:center}
.to-top{position:absolute;left:1138px;top:218px;width:26px;height:26px;background:var(--blue);display:flex;align-items:center;justify-content:center}
.bottom-bar{position:absolute;left:0;top:3337px;width:1200px;height:40px;background:var(--footer-deep);font-size:10px;color:#888;padding:12px 47px}
</style>
</head>
<body>
<div class="top-rule"></div>

<header class="site-header">
  <div class="brand"><span class="brand-dot"></span><span class="brand-name">CALDER LAW</span></div>
  <div class="brand-tag">LAW THAT UNDERSTANDS YOU</div>
  <div class="util">
    <span class="phone">
      <svg width="12" height="12" viewBox="0 0 24 24"><path d="M6.6 10.8a15 15 0 0 0 6.6 6.6l2.2-2.2c.3-.3.7-.4 1-.2 1.1.4 2.3.6 3.6.6.6 0 1 .4 1 1V20c0 .6-.4 1-1 1A17 17 0 0 1 3 4c0-.6.4-1 1-1h3.5c.6 0 1 .4 1 1 0 1.3.2 2.5.6 3.6.1.3 0 .7-.2 1z" fill="#17a98f"/></svg>
      (00) 1234 5678
    </span>
    <div class="social"><span></span><span></span><span></span><span></span></div>
  </div>
  <nav class="main-nav">
    <a style="left:0">HOME</a>
    <a style="left:83px">WHO WE ARE</a>
    <a style="left:213px">OUR SERVICES</a>
    <a style="left:348px">ARTICLES</a>
    <a style="left:452px">CONTACT US</a>
    <a style="left:582px">TERMS AND CONDITIONS</a>
  </nav>
  <svg class="search-icon" width="14" height="14" viewBox="0 0 24 24"><circle cx="10" cy="10" r="7" fill="none" stroke="#2c3a44" stroke-width="3"/><path d="M15 15l7 7" stroke="#2c3a44" stroke-width="3"/></svg>
</header>

<section class="hero" role="img" aria-label="Black and white chess pieces on a board with a king in focus">
  <h1>Guiding Successful Resolution,<br>Quickly and Intelligently</h1>
  <p>Committed to unparalleled services and client satisfaction</p>
  <div class="btn-outline">Free Consultation</div>
</section>

<h2 class="section-title" style="top:662px">WHO WE ARE</h2>
<section class="who">
  <div class="who-photo" role="img" aria-label="Business team meeting around a laptop"></div>
  <div class="who-panel">
    <p>Lorem ipsum dolor sit amet, consectetur adipiscing elit, sed do eiusmod tempor incididunt ut labore et dolore magna aliqua. Ut enim ad minim veniam, quis nostrud exercitation ullamco laboris nisi ut aliquip ex ea commodo consequat. Duis aute irure dolor in reprehenderit in voluptate velit esse cillum dolore eu fugiat nulla pariatur</p>
    <div class="btn-white">Learn more</div>
  </div>
</section>

<h2 class="section-title" style="top:1115px">OUR SERVICES</h2>

<div class="service" style="left:10px">
  <svg width="80" height="70" viewBox="0 0 80 70" fill="none" stroke="#17a98f" stroke-width="2.5"><path d="M14 34L40 12l26 22"/><path d="M22 28v22h36V28"/><path d="M34 50V38h12v12"/><path d="M6 58c14-6 24 6 36 0s22-4 32 0"/></svg>
  <h3>PROPERTY LAW</h3>
  <p>Sed ut perspiciatis unde omnis iste natus error sit voluptatem accusantium doloremque laudantium</p>
  <span class="more">Read More</span>
</div>
<div class="service" style="left:251px">
  <svg width="80" height="70" viewBox="0 0 80 70" fill="none" stroke="#17a98f" stroke-width="2.5"><rect x="24" y="6" width="32" height="56" rx="3"/><path d="M30 18h20M30 26h20M30 34h20M30 42h14"/><path d="M44 56l6-6 4 4"/></svg>
  <h3>WILLS</h3>
  <p>Sed ut perspiciatis unde omnis iste natus error sit voluptatem accusantium doloremque laudantium</p>
  <span class="more">Read More</span>
</div>
<div class="service" style="left:490px">
  <svg width="80" height="70" viewBox="0 0 80 70" fill="none" stroke="#17a98f" stroke-width="2.5"><circle cx="40" cy="14" r="8"/><path d="M36 22v12h8V22"/><rect x="22" y="34" width="36" height="10" rx="2"/><path d="M18 50h44v6H18z"/></svg>
  <h3>POWERS OF ATTORNEY</h3>
  <p>Sed ut perspiciatis unde omnis iste natus error sit voluptatem accusantium doloremque laudantium</p>
  <span class="more">Read More</span>
</div>
<div class="service" style="left:726px">
  <svg width="80" height="70" viewBox="0 0 80 70" fill="none" stroke="#17a98f" stroke-width="2.5"><rect x="22" y="6" width="22" height="56"/><rect x="44" y="22" width="16" height="40"/><path d="M28 14h4M36 14h4M28 24h4M36 24h4M28 34h4M36 34h4M28 44h4M36 44h4M50 32h4M50 42h4M16 62h50"/></svg>
  <h3>PROBATE ANDESTATE<br>ADMINISTRATION</h3>
  <p>Sed ut perspiciatis unde omnis iste natus error sit voluptatem accusantium doloremque laudantium</p>
  <span class="more">Read More</span>
</div>
<div class="service" style="left:970px">
  <svg width="80" height="70" viewBox="0 0 80 70" fill="none" stroke="#17a98f" stroke-width="2.5"><rect x="26" y="6" width="28" height="18" rx="2"/><circle cx="24" cy="38" r="6"/><circle cx="56" cy="38" r="6"/><path d="M14 60c0-8 4-12 10-12s10 4 10 12M46 60c0-8 4-12 10-12s10 4 10 12M40 24v14"/></svg>
  <h3>CONSULTANCY<br>AND AGENCY</h3>
  <p>Sed ut perspiciatis unde omnis iste natus error sit voluptatem accusantium doloremque laudantium</p>
  <span class="more">Read More</span>
</div>

<h2 class="section-title" style="top:1492px">OUR HAPPY CUSTOMERS</h2>
<section class="testimonials">
  <svg class="quote-mark" width="62" height="56" viewBox="0 0 62 56" fill="none" stroke="#17a98f" stroke-width="3"><path d="M4 4h22v24L14 52H6l8-22H4z"/><path d="M36 4h22v24L46 52h-8l8-22H36z"/></svg>
  <div class="client-name">Sam Whitford</div>
  <p class="client-quote">"Consectetur adipiscing elit, sed do eiusmod tempor incididunt ut labore et dolore magna aliqua."</p>
  <div class="slider-arrows">
    <span><svg width="10" height="12" viewBox="0 0 10 12"><path d="M8 1L2 6l6 5" fill="none" stroke="#fff" stroke-width="2"/></svg></span>
    <span><svg width="10" height="12" viewBox="0 0 10 12"><path d="M2 1l6 5-6 5" fill="none" stroke="#fff" stroke-width="2"/></svg></span>
  </div>
  <div class="client-grid" role="img" aria-label="Grid of black and white client portraits"></div>
</section>

<h2 class="section-title" style="top:2025px">OUR BLOG POSTS</h2>
<svg class="blog-arrow" style="left:26px" width="22" height="40" viewBox="0 0 22 40"><path d="M20 2L2 20l18 18" fill="none" stroke="#999" stroke-width="2"/></svg>
<article class="post" style="left:73px">
  <div class="post-photo" role="img" aria-label="Smiling businesswoman with folded arms"></div>
  <h4>At vero eos et accusamus et iusto odio dignissimos ducimus qui blanditiis.</h4>
</article>
<article class="post" style="left:441px">
  <div class="post-photo" role="img" aria-label="Two business people shaking hands"></div>
  <h4>At vero eos et accusamus et iusto odio dignissimos ducimus qui blanditiis.</h4>
</article>
<article class="post" style="left:808px">
  <div class="post-photo" role="img" aria-label="Group of business professionals standing together"></div>
  <h4>At vero eos et accusamus et iusto odio dignissimos ducimus qui blanditiis.</h4>
</article>
<svg class="blog-arrow" style="left:1152px" width="22" height="40" viewBox="0 0 22 40"><path d="M2 2l18 18L2 38" fill="none" stroke="#999" stroke-width="2"/></svg>

<h2 class="section-title" style="top:2428px">CONTACT US</h2>
<div class="map" role="img" aria-label="Street map of the city centre with the office location pinned"></div>
<svg class="abs" style="left:468px;top:2575px" width="20" height="28" viewBox="0 0 20 28"><path d="M10 0a10 10 0 0 1 10 10c0 8-10 18-10 18S0 18 0 10A10 10 0 0 1 10 0z" fill="#d9342b"/><circle cx="10" cy="10" r="3.5" fill="#7a1410"/></svg>
<form class="quote-form">
  <h3>REQUEST A QUOTE</h3>
  <div class="field" style="left:22px;top:70px;width:170px"><span>Name</span><i></i></div>
  <div class="field" style="left:203px;top:70px;width:170px"><span>Email</span><i></i></div>
  <div class="field" style="left:22px;top:120px;width:170px"><span>Phone</span><i></i></div>
  <div class="field" style="left:203px;top:120px;width:170px"><span>Subject</span><i><b>Property Law</b></i></div>
  <div class="field" style="left:22px;top:170px;width:351px"><span>Message</span><i style="height:56px"></i></div>
  <div class="send">SEND</div>
</form>

<section class="partners" aria-label="Memberships">
  <div class="badge" style="left:40px;width:120px;background:#7b3f8c" role="img" aria-label="VLQ Member"></div>
  <div class="badge" style="left:215px;width:120px;background:#8a3b86" role="img" aria-label="Coastal Women Advocates"></div>
  <div class="badge" style="left:370px;width:130px;background:#ef7d22" role="img" aria-label="Guide For Counsel"></div>
  <div class="badge" style="left:552px;width:115px;background:#1f5aa6" role="img" aria-label="Creature Foundation"></div>
  <div class="badge" style="left:720px;width:110px;background:#5a3d8a" role="img" aria-label="Tovra"></div>
  <div class="badge" style="left:876px;width:120px;background:#d9232d" role="img" aria-label="Parcelnet"></div>
  <div class="badge" style="left:1050px;width:110px;background:#6fb33f" role="img" aria-label="Vek QA"></div>
</section>

<footer class="site-footer">
  <div class="about">
    <h5>ABOUT</h5>
    <p>Sed ut perspiciatis unde omnis iste natus error sit voluptatem accusantium doloremque laudantium, totam rem aperiam, eaque ipsa quae ab illo inventore veritatis et quasi architecto beatae vitae dicta sunt explicabo.</p>
    <div class="line"><svg width="12" height="12" viewBox="0 0 24 24"><path d="M2 11L22 2l-9 20-2-9z" fill="#ddd"/></svg><span>Lorem ipsum dolor sit amet consectetur<br>adipiscing elit.</span></div>
    <div class="line"><svg width="12" height="10" viewBox="0 0 24 18"><rect x="1" y="1" width="22" height="16" fill="none" stroke="#ddd" stroke-width="2"/><path d="M1 1l11 9 11-9" fill="none" stroke="#ddd" stroke-width="2"/></svg><span>info@calderlaw.com</span></div>
    <div class="line"><svg width="12" height="12" viewBox="0 0 24 24"><path d="M6.6 10.8a15 15 0 0 0 6.6 6.6l2.2-2.2c.3-.3.7-.4 1-.2 1.1.4 2.3.6 3.6.6.6 0 1 .4 1 1V20c0 .6-.4 1-1 1A17 17 0 0 1 3 4c0-.6.4-1 1-1h3.5c.6 0 1 .4 1 1 0 1.3.2 2.5.6 3.6.1.3 0 .7-.2 1z" fill="#ddd"/></svg><span>(00) 1234 5678</span></div>
  </div>
  <div class="links">
    <h5>LINKS</h5>
    <div class="cols">
      <div>Home<br>Why Calder Law<br>Contact<br>Privacy Policy</div>
      <div>Famly Law<br>Civil Litigation<br>Conveyancing<br>Terms and Condition</div>
    </div>
    <div class="social"><span></span><span></span><span></span><span></span></div>
  </div>
  <div class="newsletter">
    <h5>Subscribe Newsletter</h5>
    <p>Subscribe to our mailing list to get the update to your email!</p>
    <div class="subscribe"><div class="input">Email</div><div class="btn">SUBMIT</div></div>
  </div>
  <div class="to-top"><svg width="12" height="8" viewBox="0 0 12 8"><path d="M1 7l5-5 5 5" fill="none" stroke="#fff" stroke-width="2"/></svg></div>
</footer>
<div class="bottom-bar">Copyright: Information here</div>
</body>
</html>
```